Meridell Financial Professional Brochure

Create a professional brochure for my financial planning team, "Meridell Financial & Insurance Solutions." Please use attached logo, attached photo's and contact information for team members, menu of services, and process. Please also leave space to add a QR code later.

```html
<!DOCTYPE html>
<html lang="en">
<head>
<meta charset="utf-8">
<title>Meridell Financial &amp; Insurance Solutions – Brochure</title>
<link href="https://fonts.googleapis.com/css2?family=Montserrat:wght@400;500;600;700;800&family=Poppins:wght@400;500;600&display=swap" rel="stylesheet">
<style>
:root{
  --blue:#1436c8;
  --blue-deep:#0a1f8f;
  --blue-bright:#1f4fff;
  --ink:#111;
  --grey:#777;
  --grey-light:#e7e7e7;
  --page:#f2f2f2;
  --white:#fff;
}
*{box-sizing:border-box;margin:0;padding:0}
html,body{width:1200px;height:2700px;overflow:hidden;background:var(--page)}
body{position:relative;font-family:"Poppins",sans-serif;color:var(--ink)}
.spread{position:absolute;left:50px;width:1100px;height:850px;background:var(--white);box-shadow:0 6px 24px rgba(0,0,0,.12);overflow:hidden}
.spread--outer{top:420px}
.spread--inner{top:1430px}
.panel{position:absolute;top:0;height:850px}
.abs{position:absolute}

/* outer spread */
.panel--team{left:0;width:365px;background:linear-gradient(#fff 30%,#f4f4f4 60%,#fff)}
.city-photo{left:0;top:0;width:365px;height:235px;background:linear-gradient(180deg,#dcdcdc,#8a8a8a 55%,#cfcfcf)}
.team-heading{left:38px;top:258px;border-left:3px solid var(--blue);padding-left:12px;font-family:"Montserrat",sans-serif;line-height:1}
.team-heading .light{font-size:24px;font-weight:500}
.team-heading .bold{font-size:31px;font-weight:800;color:var(--blue);display:block}
.member{left:30px;width:320px;height:140px}
.member .photo{position:absolute;left:0;top:0;width:104px;height:104px;border-radius:50%;background:radial-gradient(circle at 50% 40%,#bfc4cc,#6b7280);border:5px solid #c7ccd6;box-shadow:0 0 0 2px var(--blue) inset}
.member .name{position:absolute;left:117px;top:2px;font-family:"Montserrat",sans-serif;font-size:19px;font-weight:500;line-height:1.05;white-space:nowrap}
.member .name b{color:var(--blue);font-weight:800}
.member .role{position:absolute;left:117px;font-size:14px;letter-spacing:.5px;white-space:nowrap}
.member .phone{position:absolute;left:117px;font-size:15px;font-weight:600;display:flex;align-items:center;gap:8px;white-space:nowrap}
.member .mail{position:absolute;left:117px;font-size:11px;display:flex;align-items:center;gap:8px;white-space:nowrap}
.member .dash{position:absolute;left:117px;width:14px;height:2px;background:var(--blue)}
.rule{left:30px;width:310px;border-top:1px dashed #999}
.web{font-size:13px;color:var(--ink)}
.web b{color:var(--blue);font-weight:600}

.panel--contact{left:365px;width:365px;background:linear-gradient(180deg,#0c2bb0,#1a47e0 55%,#0d2fb8);border-bottom-right-radius:42px;color:var(--white)}
.brand{display:flex;align-items:center;gap:8px;font-family:"Montserrat",sans-serif;font-weight:700;letter-spacing:2px}
.brand .mark{width:12px;height:12px;background:currentColor}
.panel--contact .brand{position:absolute;left:0;right:0;justify-content:center;top:105px;font-size:24px}
.contact-item{left:0;right:0;text-align:center;font-size:16px}
.contact-icon{left:167px;width:36px;height:36px;border-radius:50%;background:var(--white);display:flex;align-items:center;justify-content:center}
.chart-art{left:0;top:525px;width:365px;height:325px;background:linear-gradient(180deg,rgba(255,255,255,0),rgba(120,200,255,.35) 60%,rgba(255,255,255,.15));border-bottom-right-radius:42px}
.follow{display:inline-flex;align-items:center;gap:6px}
.follow .sq{width:10px;height:10px;background:var(--white);border-radius:2px}

.panel--cover{left:730px;width:370px;background:var(--white)}
.panel--cover .brand{position:absolute;left:0;right:0;justify-content:center;top:112px;font-size:30px;color:var(--blue)}
.cover-tag{left:0;right:0;top:152px;text-align:center;font-size:12px;color:var(--grey);letter-spacing:1px}
.cover-frame{left:0;top:180px;width:344px;height:312px;background:var(--blue);border-top-left-radius:40px}
.cover-photo{left:4px;top:185px;width:336px;height:302px;background:linear-gradient(135deg,#8a97b8,#3d4f8f 55%,#9aa6c4);border-top-left-radius:36px}
.cover-title{left:67px;top:517px;font-family:"Montserrat",sans-serif;line-height:1}
.cover-title .small{font-size:20px;font-weight:500;letter-spacing:1px;display:block;margin-bottom:4px}
.cover-title .line{display:block;font-size:35px;font-weight:800;letter-spacing:.5px}
.cover-title .blue{color:var(--blue)}
.cover-title .thin{font-weight:500}
.dashes{left:67px;top:690px;display:flex;gap:3px}
.dashes i{width:9px;height:8px;background:var(--blue)}
.cover-text{left:69px;top:714px;width:280px;font-size:15px;line-height:1.25}

/* inner spread */
.svc{top:0;height:488px}
.svc--left{left:0;width:365px;background:linear-gradient(160deg,#0b2aa8,#1a45d8);color:var(--white)}
.svc--mid{left:365px;width:365px;background:var(--white)}
.svc--right{left:730px;width:370px;background:linear-gradient(200deg,#1a45d8,#0b2aa8);color:var(--white)}
.what-heading{left:0;right:0;top:28px;text-align:center;font-family:"Montserrat",sans-serif;font-size:30px;font-weight:500}
.what-heading b{color:var(--blue);font-weight:800}
.what-line{left:60px;top:46px;width:262px;height:1px;background:#8fa3e8}
.svc-group{position:absolute}
.svc-title{font-family:"Montserrat",sans-serif;font-weight:700;font-size:14px;display:flex;align-items:center;gap:10px;margin-left:-45px}
.svc-icon{width:33px;height:33px;border-radius:50%;background:var(--white);border:3px solid #5b80ff;display:flex;align-items:center;justify-content:center;flex:none}
.svc--mid .svc-icon{border-color:var(--blue)}
.svc-list{list-style:none;margin-top:3px}
.svc-list li{position:relative;padding-left:17px;font-size:11.5px;line-height:1.05;margin-top:7px}
.svc-list li::before{content:"";position:absolute;left:0;top:1px;width:10px;height:10px;border-radius:50%;background:#4c8dff}
.svc--mid .svc-list li::before{background:var(--blue)}
.svc-list li::after{content:"";position:absolute;left:3px;top:3.5px;width:3px;height:2px;border-left:1.5px solid #fff;border-bottom:1.5px solid #fff;transform:rotate(-45deg)}
.svc--left .svc-list li{margin-top:6px}
.svc--right .svc-list li{margin-top:9px}

.how-heading{left:44px;top:504px;font-family:"Montserrat",sans-serif;font-size:38px;font-weight:500;line-height:1}
.how-heading b{color:var(--blue-bright);font-weight:800}
.how-banner{left:367px;top:501px;width:676px;height:44px;background:var(--blue-bright);border-radius:0 12px 12px 0;color:var(--white);font-family:"Montserrat",sans-serif;font-weight:700;font-size:24px;display:flex;align-items:center;padding-left:20px}
.process{left:0;top:555px;width:1100px;height:240px}
</style>
</head>
<body>

<section class="spread spread--outer">
  <div class="panel panel--team">
    <div class="abs city-photo" role="img" aria-label="Black and white city skyline photo"></div>
    <h2 class="abs team-heading"><span class="light">OUR TEAM</span><span class="bold">MEMBERS</span></h2>

    <div class="abs member" style="top:347px">
      <div class="photo" role="img" aria-label="Portrait of Halene Voss"></div>
      <div class="name"><b>HALENE</b><br>VOSS</div>
      <div class="role" style="top:44px">Co-Founder &amp; CEO</div>
      <div class="dash" style="top:66px"></div>
      <div class="phone" style="top:72px"><svg width="14" height="14" viewBox="0 0 24 24"><path d="M6.6 10.8a15.1 15.1 0 006.6 6.6l2.2-2.2c.3-.3.7-.4 1-.2 1.1.4 2.3.6 3.6.6.6 0 1 .4 1 1V20c0 .6-.4 1-1 1A17 17 0 013 4c0-.6.4-1 1-1h3.5c.6 0 1 .4 1 1 0 1.3.2 2.5.6 3.6.1.3 0 .7-.2 1z" fill="#1436c8"/></svg>(408) 555 – 0162</div>
      <div class="mail" style="top:96px"><svg width="14" height="10" viewBox="0 0 14 10"><rect width="14" height="10" fill="#1436c8"/><path d="M0 0l7 5 7-5" stroke="#fff" fill="none"/></svg>hvoss@meridellplanning.example</div>
    </div>
    <div class="abs rule" style="top:475px"></div>

    <div class="abs member" style="top:495px">
      <div class="photo" role="img" aria-label="Portrait of Darrin Okafor"></div>
      <div class="name" style="top:24px"><b>DARRIN</b> OKAFOR</div>
      <div class="role" style="top:48px">Chief Strategic Officer</div>
      <div class="dash" style="top:70px"></div>
      <div class="phone" style="top:76px"><svg width="14" height="14" viewBox="0 0 24 24"><path d="M6.6 10.8a15.1 15.1 0 006.6 6.6l2.2-2.2c.3-.3.7-.4 1-.2 1.1.4 2.3.6 3.6.6.6 0 1 .4 1 1V20c0 .6-.4 1-1 1A17 17 0 013 4c0-.6.4-1 1-1h3.5c.6 0 1 .4 1 1 0 1.3.2 2.5.6 3.6.1.3 0 .7-.2 1z" fill="#1436c8"/></svg>(408) 555 – 0197</div>
    </div>
    <div class="abs rule" style="top:624px"></div>

    <div class="abs member" style="top:645px">
      <div class="photo" role="img" aria-label="Portrait of Tomas Wren"></div>
      <div class="name" style="top:24px"><b>TOMAS</b> WREN</div>
      <div class="role" style="top:48px">Chief Operation Officer</div>
      <div class="dash" style="top:70px"></div>
      <div class="phone" style="top:76px"><svg width="14" height="14" viewBox="0 0 24 24"><path d="M6.6 10.8a15.1 15.1 0 006.6 6.6l2.2-2.2c.3-.3.7-.4 1-.2 1.1.4 2.3.6 3.6.6.6 0 1 .4 1 1V20c0 .6-.4 1-1 1A17 17 0 013 4c0-.6.4-1 1-1h3.5c.6 0 1 .4 1 1 0 1.3.2 2.5.6 3.6.1.3 0 .7-.2 1z" fill="#1436c8"/></svg>(408) 555 – 0162</div>
    </div>
    <p class="abs web" style="left:40px;top:775px">www.<b>meridellfinancial</b>.example</p>
  </div>

  <div class="panel panel--contact">
    <div class="brand"><span class="mark"></span>MERIDELL</div>
    <div class="abs contact-icon" style="top:180px"><svg width="18" height="18" viewBox="0 0 24 24"><path d="M6.6 10.8a15.1 15.1 0 006.6 6.6l2.2-2.2c.3-.3.7-.4 1-.2 1.1.4 2.3.6 3.6.6.6 0 1 .4 1 1V20c0 .6-.4 1-1 1A17 17 0 013 4c0-.6.4-1 1-1h3.5c.6 0 1 .4 1 1 0 1.3.2 2.5.6 3.6.1.3 0 .7-.2 1z" fill="#111"/></svg></div>
    <p class="abs contact-item" style="top:219px">012.555.0147</p>
    <div class="abs contact-icon" style="top:250px"><svg width="16" height="20" viewBox="0 0 16 20"><path d="M8 0a8 8 0 00-8 8c0 6 8 12 8 12s8-6 8-12a8 8 0 00-8-8z" fill="#111"/><circle cx="8" cy="8" r="3" fill="#fff"/></svg></div>
    <p class="abs contact-item" style="top:289px">Larkmont, CA 95000, USA</p>
    <div class="abs contact-icon" style="top:325px"><svg width="18" height="13" viewBox="0 0 18 13"><rect width="18" height="13" rx="1" fill="#111"/><path d="M0 1l9 6 9-6" stroke="#fff" stroke-width="1.5" fill="none"/></svg></div>
    <p class="abs contact-item" style="top:364px">hello@meridellfinancial.example</p>
    <div class="abs contact-icon" style="top:398px"><svg width="20" height="20" viewBox="0 0 20 20"><circle cx="10" cy="10" r="9" fill="#111"/><path d="M1 10h18M10 1c-4 4-4 14 0 18M10 1c4 4 4 14 0 18M3 5h14M3 15h14" stroke="#fff" stroke-width="1.1" fill="none"/></svg></div>
    <p class="abs contact-item" style="top:436px">www.meridellfinancial.example</p>
    <p class="abs contact-item" style="top:472px;font-size:14px"><span class="follow">follow us <span class="sq"></span></span></p>
    <div class="abs chart-art" role="img" aria-label="Hand holding a tablet with a glowing bar chart rising above it"></div>
  </div>

  <div class="panel panel--cover">
    <div class="brand"><span class="mark"></span>MERIDELL</div>
    <p class="abs cover-tag">Financial &amp; Insurance Solutions</p>
    <div class="abs cover-frame"></div>
    <div class="abs cover-photo" role="img" aria-label="Three advisors smiling while working together at a laptop"></div>
    <h1 class="abs cover-title">
      <span class="small">THE VALUE OF</span>
      <span class="line">MERIDELL</span>
      <span class="line blue">FINANCIAL <span class="thin">&amp;</span></span>
      <span class="line blue">INSURANCE</span>
      <span class="line thin">SOLUTIONS</span>
    </h1>
    <div class="abs dashes"><i></i><i></i><i></i><i></i></div>
    <p class="abs cover-text">Since 2000, I've been serving loyal clients in the San Francisco area.</p>
    <p class="abs web" style="left:69px;top:775px">www.<b>meridellfinancial</b>.example</p>
  </div>
</section>

<section class="spread spread--inner">
  <div class="panel svc svc--left">
    <div class="abs what-line"></div>
    <div class="svc-group" style="left:90px;top:78px;width:255px">
      <h3 class="svc-title"><span class="svc-icon"><svg width="16" height="16" viewBox="0 0 16 16"><circle cx="8" cy="8" r="6" fill="none" stroke="#1436c8" stroke-width="2"/><path d="M8 4v8M5.5 6.5h4" stroke="#1436c8" stroke-width="1.5"/></svg></span>FINANCIAL POSITION</h3>
      <ul class="svc-list">
        <li>Recently moved or considering relocation</li>
        <li>Considering the sale of a major asset like your home or business</li>
        <li>Changing jobs</li>
        <li>Getting married or divorced</li>
        <li>Loss of a loved one</li>
        <li>Receiving a gift or inheritance</li>
      </ul>
    </div>
    <div class="svc-group" style="left:90px;top:258px;width:255px">
      <h3 class="svc-title"><span class="svc-icon"><svg width="16" height="16" viewBox="0 0 16 16"><path d="M8 1l6 2.5v4C14 11 11 14 8 15 5 14 2 11 2 7.5v-4z" fill="none" stroke="#1436c8" stroke-width="2"/></svg></span>RISK MANAGEMENT</h3>
      <ul class="svc-list">
        <li>Reviewing Health Savings Account contributions</li>
        <li>Spending and remaining balances in Flexible Spending Accounts</li>
        <li>Reviewing existing life and income disability insurance policies and coverage amounts</li>
        <li>Reviewing assisted living needs for a parent or other family member Reviewing any long-term care needs</li>
      </ul>
    </div>
  </div>

  <div class="panel svc svc--mid">
    <h2 class="abs what-heading">WHAT <b>WE DO</b></h2>
    <div class="svc-group" style="left:82px;top:85px;width:260px">
      <h3 class="svc-title"><span class="svc-icon"><svg width="14" height="16" viewBox="0 0 14 16"><rect x="1" y="1" width="12" height="14" fill="none" stroke="#1436c8" stroke-width="2"/><path d="M4 5h6M4 8h6M4 11h4" stroke="#1436c8" stroke-width="1.5"/></svg></span>TAX MANAGEMENT</h3>
      <ul class="svc-list">
        <li>Income tax strategies</li>
        <li>Alternative minimum tax strategies</li>
        <li>Capital gain/loss strategies</li>
      </ul>
    </div>
    <div class="svc-group" style="left:82px;top:188px;width:260px">
      <h3 class="svc-title"><span class="svc-icon"><svg width="16" height="16" viewBox="0 0 16 16"><circle cx="8" cy="8" r="6" fill="none" stroke="#1436c8" stroke-width="2"/><path d="M8 4v4l3 2" stroke="#1436c8" stroke-width="1.5" fill="none"/></svg></span>RETIREMENT PLANNING</h3>
      <ul class="svc-list" style="margin-top:6px">
        <li style="margin-top:9px">Retirement planning</li>
        <li style="margin-top:9px">Social security</li>
        <li style="margin-top:9px">Distribution planning</li>
        <li style="margin-top:9px">Funding analysis</li>
        <li style="margin-top:9px">Non-qualified plans</li>
        <li style="margin-top:9px">Analyzing tax benefits</li>
        <li style="margin-top:9px">Maximizing 401(k) contributions</li>
        <li style="margin-top:9px">Maximizing IRA contributions</li>
        <li style="margin-top:9px">Reviewing overall retirement income strategy</li>
        <li style="margin-top:9px">Establishing a retirement plan if a business owner</li>
      </ul>
    </div>
  </div>

  <div class="panel svc svc--right">
    <svg class="abs" style="left:290px;top:0" width="80" height="488" viewBox="0 0 80 488" aria-hidden="true">
      <path d="M28 0h24v70h-24z" fill="#d9d9d9"/>
      <path d="M40 20L80 70H0z" fill="#a8a8a8"/>
      <path d="M28 70h24v300L80 488H0l28-118z" fill="#c4c4c4" opacity=".85"/>
    </svg>
    <div class="svc-group" style="left:63px;top:85px;width:225px">
      <h3 class="svc-title"><span class="svc-icon"><svg width="16" height="16" viewBox="0 0 16 16"><path d="M2 14V9M6 14V6M10 14V8M14 14V3" stroke="#1436c8" stroke-width="2.2"/></svg></span>WEALTH ACCUMULATION</h3>
      <ul class="svc-list">
        <li>Confirming investment goals &amp; strategies</li>
        <li style="margin-top:12px">Reviewing asset allocation</li>
        <li style="margin-top:12px">Revisiting income &amp; savings needs</li>
        <li style="margin-top:12px">Contributing to education accounts</li>
        <li style="margin-top:12px">Establishing savings plan for major purchase or expense goal</li>
      </ul>
    </div>
    <div class="svc-group" style="left:63px;top:260px;width:225px">
      <h3 class="svc-title"><span class="svc-icon"><svg width="14" height="16" viewBox="0 0 14 16"><rect x="1" y="1" width="12" height="14" fill="none" stroke="#1436c8" stroke-width="2"/><path d="M4 6h6M4 10h6" stroke="#1436c8" stroke-width="1.5"/></svg></span>ESTATE PLANNING</h3>
      <ul class="svc-list">
        <li>Using a trust</li>
        <li>Reviewing beneficiary designations</li>
        <li>Planning charitable giving</li>
        <li>Reviewing impact of any new tax laws</li>
        <li>Reviewing estate documents (wills, trusts)</li>
        <li>Planning for the succession of a business</li>
        <li>Analyzing estate tax implications</li>
      </ul>
    </div>
  </div>

  <h2 class="abs how-heading">HOW <b>WE DO IT</b></h2>
  <div class="abs how-banner">Your unique vision with our systematic approach</div>

  <svg class="abs process" viewBox="0 555 1100 240" width="1100" height="240" font-family="Montserrat, sans-serif" aria-label="Six-step planning process">
    <g fill="#bdbdbd">
      <path d="M47 563h110l8 10-8 10H47l6-10z"/>
      <path d="M160 563h378l8 10-8 10H160l8-10z"/>
      <path d="M541 563h258l8 10-8 10H541l8-10z"/>
      <path d="M802 563h243l8 10-8 10H802l8-10z"/>
    </g>
    <g font-size="10" font-weight="600" fill="#222" text-anchor="middle">
      <text x="104" y="577">ENGAGE</text>
      <text x="353" y="577">ASSESS</text>
      <text x="676" y="577">EXECUTE</text>
      <text x="925" y="577">ONGOING PLANNING RELATIONSHIP</text>
    </g>
    <g>
      <path d="M47 632h115l18 40-18 40H47z" fill="#1f4fff"/>
      <path d="M176 632h115l18 40-18 40H176z" fill="#1f4fff"/>
      <path d="M304 632h115l18 40-18 40H304z" fill="#8a8a8a"/>
      <path d="M433 632h115l18 40-18 40H433z" fill="#1f4fff"/>
      <path d="M562 632h115l18 40-18 40H562z" fill="#1f4fff"/>
      <path d="M690 632h118l18 40-18 40H690z" fill="#1f4fff"/>
      <path d="M60 712h95l-15 22H75z" fill="#d9d9d9" opacity=".6"/>
    </g>
    <g fill="#fff" stroke="#e3e3e3">
      <rect x="55" y="625" width="95" height="115" rx="5"/>
      <rect x="184" y="625" width="95" height="115" rx="5"/>
      <rect x="312" y="625" width="95" height="115" rx="5"/>
      <rect x="441" y="625" width="95" height="115" rx="5" fill="#e2e2e2"/>
      <rect x="570" y="625" width="95" height="115" rx="5"/>
      <rect x="698" y="625" width="95" height="115" rx="5"/>
    </g>
    <g fill="#fff" stroke="#555">
      <circle cx="102" cy="611" r="8"/><circle cx="231" cy="611" r="8"/><circle cx="359" cy="611" r="8"/>
      <circle cx="617" cy="611" r="8"/><circle cx="745" cy="611" r="8"/><circle cx="895" cy="611" r="8"/>
    </g>
    <g font-size="10" fill="#222" text-anchor="middle" font-family="Poppins, sans-serif">
      <text x="102" y="615">1</text><text x="231" y="615">2</text><text x="359" y="615">3</text>
      <text x="617" y="615">4</text><text x="745" y="615">5</text><text x="895" y="615">6</text>
    </g>
    <g fill="#666">
      <circle cx="96" cy="663" r="6"/><path d="M86 686a10 9 0 0120 0z"/><circle cx="110" cy="667" r="5"/>
      <circle cx="231" cy="660" r="4"/><circle cx="219" cy="672" r="4"/><circle cx="243" cy="672" r="4"/><path d="M224 685h14v-6h-14z"/>
      <rect x="347" y="655" width="24" height="28" fill="none" stroke="#666" stroke-width="2"/><path d="M352 678v-6M358 678v-10M364 678v-14" stroke="#666" stroke-width="2"/>
      <rect x="603" y="656" width="28" height="20" fill="none" stroke="#666" stroke-width="2"/><path d="M617 676v8M609 684h16" stroke="#666" stroke-width="2"/>
      <circle cx="740" cy="664" r="8" fill="none" stroke="#666" stroke-width="2"/><circle cx="752" cy="680" r="5"/>
    </g>
    <g font-size="11" font-weight="600" fill="#111" text-anchor="middle">
      <text x="102" y="708">Engagement</text><text x="102" y="721">Meeting</text>
      <text x="231" y="708">Data Gathering</text><text x="231" y="721">Meeting</text>
      <text x="359" y="708">Analyze</text><text x="359" y="721">Information</text>
      <text x="488" y="680">STRATEGY</text><text x="488" y="692">CHECK-IN</text>
      <text x="617" y="708">Plan</text><text x="617" y="721">Presentation</text>
      <text x="745" y="708">Implementation</text>
    </g>
    <g>
      <path d="M812 640h230l12 50-12 50H812z" fill="#1f4fff"/>
      <rect x="818" y="626" width="100" height="56" rx="10" fill="#fff" stroke="#1f4fff" stroke-width="2"/>
      <rect x="932" y="626" width="100" height="56" rx="10" fill="#fff" stroke="#1f4fff" stroke-width="2"/>
      <rect x="818" y="698" width="100" height="56" rx="10" fill="#fff" stroke="#1f4fff" stroke-width="2"/>
      <rect x="932" y="698" width="100" height="56" rx="10" fill="#fff" stroke="#1f4fff" stroke-width="2"/>
      <circle cx="925" cy="690" r="48" fill="#fff" stroke="#1f4fff" stroke-width="3"/>
      <rect x="884" y="683" width="6" height="6" fill="#1f4fff"/>
      <text x="931" y="690" font-size="12" font-weight="700" fill="#1f4fff" text-anchor="middle" letter-spacing="1">MERIDELL</text>
      <g font-size="9" font-weight="600" fill="#111">
        <text x="826" y="646"><tspan fill="#1f4fff">Q1 :</tspan> Financial</text><text x="826" y="656">Planning</text><text x="826" y="666">Topics</text>
        <text x="1024" y="646" text-anchor="end" fill="#1f4fff">Q2 :</text><text x="1024" y="656" text-anchor="end">Investment</text><text x="1024" y="666" text-anchor="end">Planning</text>
        <text x="826" y="716" fill="#1f4fff">Q4 :</text><text x="826" y="726">Yr. End</text><text x="826" y="736">Tax Planning</text>
        <text x="1024" y="716" text-anchor="end" fill="#1f4fff">Q3 :</text><text x="1024" y="726" text-anchor="end">Protection</text><text x="1024" y="736" text-anchor="end">Planning</text>
      </g>
    </g>
  </svg>
</section>

</body>
</html>
```